I need to add on from our previous project a couple extra signs

We need to create two signs from your original desgin with a arrow saying 600M on the left.
also another sign drawn up similar to the one attached but also adding in there that the containers are 20ft/40ft and we have caravan, car and boat storage.
also add on the sign something for " sign online or call the number to rent space"

```html
<!DOCTYPE html>
<html lang="en">
<head>
<meta charset="utf-8">
<title>Keystone Storage – Roadside Signs</title>
<link rel="stylesheet" href="https://fonts.googleapis.com/css2?family=Orbitron:wght@800;900&family=Poppins:wght@400;500;600;700;800&display=swap">
<style>
  :root{
    --red:#cc1f28;
    --ink:#2a2627;
    --white:#ffffff;
    --rule:#e2e2e2;
    --shadow:rgba(40,50,70,.22);
  }
  *{box-sizing:border-box;margin:0;padding:0}
  html,body{width:1200px;height:1200px;overflow:hidden;background:var(--white)}
  .canvas{position:relative;width:1200px;height:1200px;font-family:"Poppins",sans-serif;color:var(--ink)}
  .sign{position:absolute;background:var(--white);box-shadow:0 0 6px var(--shadow)}
  .sign--distance{left:121px;top:177px;width:965px;height:482px}
  .sign--info{left:121px;top:732px;width:965px;height:280px}
  .sign svg{position:absolute;left:0;top:0;width:100%;height:100%}
  .txt{position:absolute;line-height:1;white-space:nowrap}
  .display{font-family:"Orbitron",sans-serif;font-weight:900}
  .red{color:var(--red)}
  .ink{color:var(--ink)}
  .white{color:var(--white)}

  /* distance sign */
  .distance{left:181px;top:293px;font-size:104px;letter-spacing:2px}
  .direction{left:183px;top:409px;font-size:55px;letter-spacing:-1px}
  .web-large{left:185px;top:531px;font-size:26px;font-weight:500}
  .brand-mark{position:absolute;border-radius:50%;border:7px solid var(--red)}
  .brand-mark--large{left:654px;top:406px;width:88px;height:88px}
  .brand-mark--small{left:174px;top:770px;width:50px;height:50px;border-width:4px}
  .brand-name{font-family:"Orbitron",sans-serif;font-weight:900;color:var(--ink)}
  .brand-name--large{left:751px;top:404px;font-size:30px;line-height:1.05}
  .phone-large{left:753px;top:479px;font-family:"Orbitron",sans-serif;font-weight:800;font-size:16px;letter-spacing:2px}

  /* info sign */
  .brand-name--small{left:229px;top:767px;font-size:17px;line-height:1.02}
  .web-small{left:230px;top:803px;font-size:6.5px;font-weight:500}
  .phone-small{left:230px;top:812px;font-family:"Orbitron",sans-serif;font-weight:800;font-size:8px;letter-spacing:1px}
  .why{left:177px;top:836px;font-size:26px;letter-spacing:-.5px}
  .containers-label{left:177px;top:909px;font-size:21px;font-weight:400}
  .containers-size{left:177px;top:939px;font-size:37px}
  .check-line{left:576px;top:756px;font-size:23px;font-weight:800}
  .availability{left:576px;top:780px;font-size:33px;font-weight:800;letter-spacing:.5px}
  .call-line{left:576px;top:812px;font-size:21px;font-weight:400}
  .phone-main{left:606px;top:839px;font-size:27px;font-weight:700;letter-spacing:1.5px}
  .extras-title{left:876px;top:757px;font-size:16px;font-weight:700}
  .extras-list{position:absolute;left:877px;top:781px;list-style:none}
  .extras-list li{display:flex;align-items:center;gap:6px;height:23px;font-size:16px;font-weight:500;color:var(--white)}
  .extras-list svg{width:14px;height:14px;flex:none}
  .free-title{left:576px;top:890px;font-size:16.5px;font-weight:700}
  .hazard{position:absolute;top:959px;width:130px;text-align:center;font-size:21px;font-weight:800;line-height:1}
  .hazard--vermin{left:554px}
  .hazard--insect{left:681px}
  .hazard--water{left:810px}
  .hazard--dust{left:924px}
</style>
</head>
<body>
<div class="canvas">

  <section class="sign sign--distance" aria-label="Distance sign">
    <svg viewBox="194 283 1544 772" aria-hidden="true">
      <path fill="var(--red)" d="M868,283 L958,283 C1030,390 1065,510 1065,620 L993,620 C993,510 950,390 868,283 Z"/>
      <path fill="var(--ink)" d="M962,812 L1038,812 C1010,900 960,985 895,1055 L787,1055 C870,985 930,900 962,812 Z"/>
      <polygon fill="var(--red)" points="1534,428 1645,428 1589,325"/>
      <polygon fill="var(--ink)" points="1520,473 1659,473 1589,347"/>
      <rect fill="var(--ink)" x="1556" y="470" width="68" height="585"/>
    </svg>
  </section>

  <div class="txt display distance"><span class="red">600</span><span class="ink">m</span></div>
  <div class="txt display direction"><span class="ink">ON</span> <span class="red">LEFT</span></div>
  <div class="txt web-large ink">www.keystonestorage.com.au</div>
  <span class="brand-mark brand-mark--large"></span>
  <div class="txt brand-name brand-name--large">KEYSTONE<br>STORAGE</div>
  <div class="txt phone-large red">(03) 5550 0142</div>

  <section class="sign sign--info" aria-label="Information sign">
    <svg viewBox="194 1172 1544 448" aria-hidden="false">
      <path fill="var(--red)" d="M722,1172 L795,1172 C840,1240 865,1310 867,1375 L808,1375 C805,1300 775,1230 722,1172 Z"/>
      <path fill="var(--ink)" d="M194,1412 L867,1412 C855,1490 830,1560 790,1620 L194,1620 Z"/>
      <path fill="var(--red)" style="filter:drop-shadow(0 7px 4px rgba(0,0,0,.35))" d="M1371,1172 H1648 V1350 Q1648,1383 1615,1383 H1404 Q1371,1383 1371,1350 Z"/>
      <path fill="none" stroke="var(--red)" stroke-width="2.5" d="M1512,1432 H1620 Q1647,1432 1647,1460 V1530"/>
      <g stroke="var(--rule)" stroke-width="2">
        <line x1="1093" y1="1470" x2="1093" y2="1580"/>
        <line x1="1298" y1="1470" x2="1298" y2="1580"/>
        <line x1="1502" y1="1470" x2="1502" y2="1580"/>
      </g>
      <g fill="var(--red)">
        <path d="M941,1355 q-8,8 0,24 q10,16 26,22 q8,2 12,-5 l-8,-7 q-5,5 -9,1 q-8,-6 -12,-14 q-3,-5 2,-8 l-5,-10 q-3,-5 -6,-3 Z"/>
        <path d="M960,1352 a14,14 0 0 1 13,13" fill="none" stroke="var(--red)" stroke-width="3"/>
      </g>
      <g role="img" aria-label="Vermin icon" fill="var(--red)"><ellipse cx="990" cy="1502" rx="28" ry="17"/></g>
      <g role="img" aria-label="Insect icon" fill="var(--red)"><ellipse cx="1193" cy="1505" rx="18" ry="24"/></g>
      <g role="img" aria-label="Water drops icon" fill="var(--red)">
        <path d="M1402,1490 C1392,1505 1387,1512 1387,1518 a15,15 0 0 0 30,0 C1417,1512 1412,1505 1402,1490 Z"/>
        <path d="M1384,1474 C1379,1482 1376,1486 1376,1490 a8,8 0 0 0 16,0 C1392,1486 1389,1482 1384,1474 Z"/>
        <path d="M1416,1472 C1412,1478 1410,1481 1410,1484 a6,6 0 0 0 12,0 C1422,1481 1420,1478 1416,1472 Z"/>
      </g>
      <g role="img" aria-label="Dust cloud icon" fill="var(--red)"><circle cx="1582" cy="1500" r="22"/><circle cx="1560" cy="1522" r="4"/><circle cx="1605" cy="1478" r="4"/></g>
    </svg>
  </section>

  <span class="brand-mark brand-mark--small"></span>
  <div class="txt brand-name brand-name--small">KEYSTONE<br>STORAGE</div>
  <div class="txt web-small ink">www.keystonestorage.com.au</div>
  <div class="txt phone-small red">(03) 5550 0142</div>
  <div class="txt display why"><span class="red">WHY CHOOSE</span> <span class="ink">US?</span></div>
  <div class="txt containers-label white">OUR CONTAINERS ARE</div>
  <div class="txt display containers-size white">20FT/40FT</div>

  <div class="txt check-line red">CHECK ONLINE FOR</div>
  <div class="txt availability red">AVAILABILITY</div>
  <div class="txt call-line ink">OR CALL THIS NUMBER</div>
  <div class="txt phone-main ink">(03) 5550 0143</div>

  <div class="txt extras-title white">WE ALSO HAVE</div>
  <ul class="extras-list">
    <li><svg viewBox="0 0 14 14"><rect x="1" y="2" width="11" height="11" rx="2" fill="none" stroke="#fff" stroke-width="1.6"/><path d="M3,7 L6,10 L13,1" fill="none" stroke="var(--ink)" stroke-width="2.4"/></svg>Caravan</li>
    <li><svg viewBox="0 0 14 14"><rect x="1" y="2" width="11" height="11" rx="2" fill="none" stroke="#fff" stroke-width="1.6"/><path d="M3,7 L6,10 L13,1" fill="none" stroke="var(--ink)" stroke-width="2.4"/></svg>Car</li>
    <li><svg viewBox="0 0 14 14"><rect x="1" y="2" width="11" height="11" rx="2" fill="none" stroke="#fff" stroke-width="1.6"/><path d="M3,7 L6,10 L13,1" fill="none" stroke="var(--ink)" stroke-width="2.4"/></svg>Boat storage</li>
  </ul>

  <div class="txt free-title ink">SHIPPING CONTAINERS ARE FREE FROM</div>
  <div class="hazard hazard--vermin ink">VERMIN</div>
  <div class="hazard hazard--insect ink">INSECT</div>
  <div class="hazard hazard--water ink">WATER</div>
  <div class="hazard hazard--dust ink">DUST</div>

</div>
</body>
</html>
```